Velora Pedalworks

We are a new start up company selling (online) innovative cycling products.
Being a new player in the market a modern eye catching logo would be good.
Initially selling safety tail lights with blinkers & modern designed cycling gloves and eventually extending our range into cycling clothing. Many of our products will have a safety theme.

Please see logo attached.

Reason: I have extended deadline because i have just received the Logo to be used.

Target Market(s)

We will be target marketing to the young 20-30year old trendy commuter cyclists to the 40 - 60 year old weekend road riders with there immaculate color coordinated road bikes & clothing.

Industry/Entity Type

Safety

Requirements
Must have
• Name: Mavin Tolby
Line for Mobile No. 0438 261 905
Line for email Address: mavin@velorapedalworks.example.com.au
3 Lines for Postal Address: PO Box 3862
Wattle Crest Corner
NSW 2174
Website: www.velorapedalworks.example.com.au

```html
<!DOCTYPE html>
<html lang="en">
<head>
<meta charset="utf-8">
<title>Velora Pedalworks – Business Card</title>
<link rel="stylesheet" href="https://fonts.googleapis.com/css2?family=Hind:wght@400;600&display=swap">
<style>
  :root {
    --backdrop: #1c3f86;
    --card-white: #ffffff;
    --card-yellow: #fdc800;
    --brand-orange: #f47a12;
    --ink: #111111;
  }
  html, body {
    margin: 0;
    padding: 0;
    width: 1200px;
    height: 1000px;
    overflow: hidden;
    background: var(--backdrop);
    font-family: "Hind", "Trebuchet MS", sans-serif;
  }
  .business-card {
    position: absolute;
    left: 239px;
    top: 293px;
    width: 721px;
    height: 416px;
    border-radius: 14px;
    overflow: hidden;
    background: var(--card-white);
  }
  .card-split {
    position: absolute;
    inset: 0;
    width: 100%;
    height: 100%;
  }
  .card-split .yellow-field { fill: var(--card-yellow); }
  .brand-lockup {
    position: absolute;
    left: 62px;
    top: 96px;
    display: flex;
    align-items: center;
    gap: 12px;
  }
  .brand-dot {
    width: 26px;
    height: 26px;
    border-radius: 50%;
    background: var(--brand-orange);
  }
  .brand-name {
    font-size: 31px;
    font-weight: 600;
    color: var(--brand-orange);
    letter-spacing: 0.2px;
  }
  .contact-block {
    position: absolute;
    right: 38px;
    top: 174px;
    text-align: right;
    color: var(--ink);
    font-size: 18px;
    line-height: 23px;
  }
  .contact-name {
    font-size: 23px;
    font-weight: 600;
    margin: 0 0 36px;
  }
  .contact-group { margin: 0 0 11px; }
  .contact-group p { margin: 0; }
</style>
</head>
<body>
  <article class="business-card">
    <svg class="card-split" viewBox="0 0 721 416" aria-hidden="true">
      <polygon class="yellow-field" points="666,0 721,0 721,416 48,416"/>
    </svg>

    <div class="brand-lockup">
      <span class="brand-dot"></span>
      <span class="brand-name">Velora Pedalworks</span>
    </div>

    <div class="contact-block">
      <p class="contact-name">Mavin Tolby</p>
      <div class="contact-group">
        <p>0438 261 905</p>
        <p>mavin@velorapedalworks.example.com.au</p>
      </div>
      <div class="contact-group">
        <p>PO Box 3862</p>
        <p>Wattle Crest Corner</p>
        <p>NSW 2174</p>
        <p>www.velorapedalworks.example.com.au</p>
      </div>
    </div>
  </article>
</body>
</html>
```